RB Business Card Design

My company provides advising/training and coaching services to business owners who want better financial results and better work/life balance. We help them through creating custom plans supported with education, strategic thinking and accountability.

We also help through some online courses which are geared to smaller businesses.
Updates

please also include our nth american contact # +1 555 382 6071

Industry/Entity Type

Financial

Contact Information for Business Card

Perry Valdane
perry@perryvaldane.net
+61 455 713 902
www.perryvaldane.net

```html
<!DOCTYPE html>
<html lang="en">
<head>
<meta charset="utf-8">
<title>Perry Valdane – Business Cards</title>
<link href="https://fonts.googleapis.com/css2?family=Arimo:wght@400;700&display=swap" rel="stylesheet">
<style>
  :root {
    --page-bg: #d9dbe0;
    --card-bg: #050507;
    --accent-blue: #1f7fe0;
    --ghost: #14151a;
  }
  * { box-sizing: border-box; margin: 0; padding: 0; }
  html, body {
    width: 1200px; height: 960px; overflow: hidden;
    background: var(--page-bg);
    font-family: "Arimo", Arial, sans-serif;
  }
  .stage {
    width: 1200px; height: 960px;
    display: flex; align-items: center; justify-content: center; gap: 90px;
  }
  .card {
    position: relative;
    width: 400px; height: 680px;
    background: var(--card-bg);
    border-radius: 4px;
    box-shadow: 0 12px 30px rgba(0,0,0,0.25);
    overflow: hidden;
    color: var(--accent-blue);
  }
  .ghost-mark {
    position: absolute;
    border-radius: 50%;
    background: var(--ghost);
  }
  .card-front .ghost-mark { left: 50px; top: 70px; width: 300px; height: 300px; }
  .card-back .ghost-mark { left: 50px; top: 400px; width: 220px; height: 220px; }

  .brand {
    display: flex; align-items: center; gap: 12px;
    font-weight: 400; font-size: 26px; letter-spacing: 0.5px;
    color: var(--accent-blue);
    text-transform: uppercase;
    white-space: nowrap;
  }
  .brand-dot {
    width: 32px; height: 32px; border-radius: 50%;
    background: var(--accent-blue); flex: none;
  }

  .card-front .brand { position: absolute; left: 40px; right: 40px; bottom: 120px; }
  .tagline {
    position: absolute; left: 40px; right: 30px; bottom: 76px;
    font-size: 17px; color: var(--accent-blue); white-space: nowrap;
  }
  .tagline strong { font-weight: 700; }

  .card-back .brand { position: absolute; left: 40px; right: 40px; top: 70px; }
  .contact-list {
    position: absolute; left: 40px; right: 30px; top: 170px;
    list-style: none;
  }
  .contact-list li {
    display: flex; align-items: center; gap: 16px;
    font-size: 20px; height: 42px; white-space: nowrap;
  }
  .contact-list svg { width: 20px; height: 20px; flex: none; fill: var(--accent-blue); }
</style>
</head>
<body>
<main class="stage">
  <section class="card card-front" aria-label="Card front">
    <div class="ghost-mark" aria-hidden="true"></div>
    <div class="brand"><span class="brand-dot"></span>Perry Valdane</div>
    <p class="tagline">Knowledge + Planning * Action = <strong>Success</strong></p>
  </section>

  <section class="card card-back" aria-label="Card back">
    <div class="brand"><span class="brand-dot"></span>Perry Valdane</div>
    <ul class="contact-list">
      <li>
        <svg viewBox="0 0 24 24" aria-hidden="true"><path d="M6.6 10.8a15.1 15.1 0 0 0 6.6 6.6l2.2-2.2a1 1 0 0 1 1-.25 11.4 11.4 0 0 0 3.6.57 1 1 0 0 1 1 1V20a1 1 0 0 1-1 1A17 17 0 0 1 3 4a1 1 0 0 1 1-1h3.5a1 1 0 0 1 1 1c0 1.25.2 2.45.57 3.6a1 1 0 0 1-.25 1z"/></svg>
        +1 555 382 6071
      </li>
      <li>
        <svg viewBox="0 0 24 24" aria-hidden="true"><path d="M6.6 10.8a15.1 15.1 0 0 0 6.6 6.6l2.2-2.2a1 1 0 0 1 1-.25 11.4 11.4 0 0 0 3.6.57 1 1 0 0 1 1 1V20a1 1 0 0 1-1 1A17 17 0 0 1 3 4a1 1 0 0 1 1-1h3.5a1 1 0 0 1 1 1c0 1.25.2 2.45.57 3.6a1 1 0 0 1-.25 1z"/></svg>
        +61 455 713 902
      </li>
      <li>
        <svg viewBox="0 0 24 24" aria-hidden="true"><path d="M2 5h20v14H2z M2 5l10 8 10-8" fill="none" stroke="#1f7fe0" stroke-width="2"/></svg>
        perry@perryvaldane.net
      </li>
      <li>
        <svg viewBox="0 0 24 24" aria-hidden="true"><circle cx="12" cy="12" r="9" fill="none" stroke="#1f7fe0" stroke-width="2"/><path d="M3 12h18M12 3c3 3 3 15 0 18M12 3c-3 3-3 15 0 18" fill="none" stroke="#1f7fe0" stroke-width="1.6"/></svg>
        www.perryvaldane.net
      </li>
    </ul>
    <div class="ghost-mark" aria-hidden="true"></div>
  </section>
</main>
</body>
</html>
```